Corrandel Ice Creamery tourist signage

We need to give passing tourists a snapshot of what great fun they can have visiting our brand new Ice creamery located in Timboon, 17km North of the Great Ocean Road and Famous 12 Apostles in Victoria Australia. So the sign needs to be more than directional, need to be enticing. needs to be designed in a manner that project quality. ( keep in mind cars travelling at 80km don't have a lot of time to read too much)
Size is 2.2metres wide by 1.4 meters high
This sign needs to be succinct. Needs to convey fun and a little indulgence but not in a 'tacky' or 'cheap' way.
Needs to offer indulgent imagery of course, our logo too and direction.

Target Market(s)

Tourists, domestic and internationals

Industry/Entity Type

Tourism

Other font styles liked:
• sacred cow

Colors
add136
fdf3f8
b8a6cd
fabb94
fcca95
85acd3
fbf289

Requirements
Must have
• Convey fun, whimsy indulgence and value ( keeping in mind we need to entice these people a further 17km up the road!)
Nice to have
• White space and clear imagery with
Should not have
• Bold bling colours, be busy looking and cheap looking, needs to convey quality .

```html
<!DOCTYPE html>
<html lang="en">
<head>
<meta charset="utf-8">
<title>Corrandel Ice Creamery – Roadside Sign</title>
<link href="https://fonts.googleapis.com/css2?family=Lato:wght@900&display=swap" rel="stylesheet">
<style>
  :root {
    --paper: #ffffff;
    --band-red: #a8262b;
    --band-red-light: #b5302f;
    --band-text: #ffffff;
    --brand-ink: #1f1f1f;
    --brand-green: #add136;
    --photo-hair: #8a5a3a;
    --photo-skin: #f2c9b0;
    --photo-dress: #e9a9c2;
    --photo-stripe: #5f6fa8;
  }
  * { margin: 0; padding: 0; box-sizing: border-box; }
  html, body {
    width: 1200px;
    height: 764px;
    overflow: hidden;
    background: var(--paper);
  }
  .sign {
    position: relative;
    width: 1200px;
    height: 764px;
    background: var(--paper);
    overflow: hidden;
    font-family: "Lato", Arial, sans-serif;
  }
  .distance-band {
    position: absolute;
    left: 315px;
    top: 68px;
    width: 885px;
    height: 362px;
    background: linear-gradient(90deg, var(--band-red) 0%, var(--band-red-light) 60%, var(--band-red) 100%);
  }
  .distance-text {
    position: absolute;
    left: 520px;
    top: 68px;
    width: 650px;
    height: 362px;
    display: flex;
    flex-direction: column;
    justify-content: center;
    align-items: center;
    color: var(--band-text);
    font-weight: 900;
    font-size: 152px;
    line-height: 150px;
    letter-spacing: 1px;
    text-align: center;
  }
  .hero-photo {
    position: absolute;
    left: 0;
    top: 0;
    width: 530px;
    height: 764px;
  }
  .brand {
    position: absolute;
    left: 600px;
    top: 490px;
    width: 540px;
    height: 240px;
  }
  .brand-dot {
    position: absolute;
    left: 170px;
    top: 0;
    width: 210px;
    height: 210px;
    border-radius: 50%;
    background: var(--brand-green);
  }
  .brand-name {
    position: absolute;
    left: 0;
    top: 52px;
    width: 540px;
    text-align: center;
    color: var(--brand-ink);
    font-weight: 900;
    font-size: 62px;
    line-height: 64px;
    letter-spacing: 3px;
    text-transform: uppercase;
  }
  .brand-name .brand-line-small {
    display: block;
    font-size: 30px;
    line-height: 40px;
    letter-spacing: 6px;
  }
</style>
</head>
<body>
  <main class="sign">
    <div class="distance-band"></div>

    <svg class="hero-photo" viewBox="0 0 530 764" role="img"
         aria-label="Photo of a smiling young girl with long hair and a pink flower headband, licking a pink ice cream cone">
      <defs>
        <linearGradient id="photoTone" x1="0" y1="0" x2="0" y2="1">
          <stop offset="0" stop-color="var(--photo-hair)"/>
          <stop offset="0.35" stop-color="var(--photo-skin)"/>
          <stop offset="0.7" stop-color="var(--photo-dress)"/>
          <stop offset="1" stop-color="var(--photo-stripe)"/>
        </linearGradient>
      </defs>
      <path d="M40 764 C20 600 10 420 60 260 C90 120 160 30 250 30 C340 30 400 110 420 230 C440 320 470 360 500 420 C530 500 520 620 510 764 Z"
            fill="url(#photoTone)"/>
    </svg>

    <div class="distance-text">
      <span>17 KM</span>
      <span>AHEAD</span>
    </div>

    <div class="brand">
      <div class="brand-dot"></div>
      <p class="brand-name">Corrandel<span class="brand-line-small">Ice Creamery</span></p>
    </div>
  </main>
</body>
</html>
```